Business Card Design

We are a new residential construction company.our team is made up of young highly skilled tradesman of the next generation of carpenters coming through with new skills and ideas.we chose the name meridian as it means strikingly different from the rest as this is what we plan to be and we would like to portray this in our business card.we like Bold lettering as we want to make a statement, also the use of colour would be great as we want to stand out from the usual plain construction cards and logos.
I have attached a logo sketch I did as a rough idea if you can tidy it up or improve on it would be good.
I have also attached the LBP logo please include this on the card small but still legible.
open to any colourschemes ideas.
thanks
(note)please delete the LBP#804317 off from the card details please.
Industry/Entity Type
Construction
Contact Information for Business Card
MERIDIAN CONSTRUCTION LIMITED
Director:Tom Halvick
Mobile :0217364820
Email:Meridian.Construction@quillpost.example
Address:48 Wendle place,Ashgrove park 2091,Auckland
LBP#BP804317

```html
<!DOCTYPE html>
<html lang="en">
<head>
<meta charset="utf-8">
<title>Meridian Construction – Business Card</title>
<link rel="stylesheet" href="https://fonts.googleapis.com/css2?family=Ubuntu:wght@400;500;700&display=swap">
<style>
  :root {
    --backdrop: #d9d9d9;
    --card-dark: #050505;
    --card-mid: #1c1c1e;
    --brand-blue: #4f5fd6;
    --label-blue: #5a66c8;
    --text-light: #f2f2f2;
    --text-soft: #d6d6d6;
    --badge-fill: #e9e9e9;
    --badge-ring: #8a8a8a;
  }
  * { box-sizing: border-box; margin: 0; padding: 0; }
  html, body {
    width: 1200px;
    height: 861px;
    overflow: hidden;
    background: var(--backdrop);
    font-family: "Ubuntu", Arial, sans-serif;
  }
  .canvas {
    position: relative;
    width: 1200px;
    height: 861px;
  }
  .card {
    position: absolute;
    width: 530px;
    height: 303px;
    border-radius: 4px;
    overflow: hidden;
    box-shadow: 0 10px 28px rgba(0,0,0,0.28);
  }
  .card-surface {
    position: absolute;
    inset: 0;
    background:
      linear-gradient(118deg, rgba(255,255,255,0) 0%, rgba(255,255,255,0) 22%, rgba(255,255,255,0.07) 22.5%, rgba(255,255,255,0.02) 60%, rgba(255,255,255,0) 100%),
      linear-gradient(160deg, var(--card-mid) 0%, var(--card-dark) 100%);
  }
  .card--details { left: 50px; top: 279px; }
  .card--brand { left: 620px; top: 279px; }

  .brand-name {
    position: absolute;
    color: var(--brand-blue);
    font-weight: 700;
    text-transform: uppercase;
    line-height: 1;
    letter-spacing: 0.02em;
  }
  .card--details .brand-name {
    left: 170px;
    top: 34px;
    font-size: 30px;
  }
  .card--details .brand-name small {
    display: block;
    font-size: 15px;
    letter-spacing: 0.12em;
    margin-top: 3px;
  }
  .lbp-badge {
    position: absolute;
    right: 32px;
    top: 32px;
    width: 62px;
    height: 62px;
  }
  .holder {
    position: absolute;
    left: 34px;
    top: 150px;
  }
  .holder-name {
    color: var(--text-light);
    font-size: 30px;
    font-weight: 500;
    line-height: 1;
  }
  .holder-role {
    color: var(--label-blue);
    font-size: 14px;
    font-weight: 500;
    letter-spacing: 0.04em;
    margin-top: 3px;
  }
  .contact-list {
    position: absolute;
    left: 60px;
    top: 208px;
    display: grid;
    grid-template-columns: 56px auto;
    row-gap: 3px;
    font-size: 12.5px;
    line-height: 1.35;
  }
  .contact-list dt { color: var(--label-blue); }
  .contact-list dd { color: var(--text-soft); }

  .card--brand .brand-lockup {
    position: absolute;
    inset: 0;
    display: flex;
    flex-direction: column;
    align-items: center;
    justify-content: center;
  }
  .card--brand .brand-name {
    position: static;
    font-size: 68px;
  }
  .card--brand .brand-name.sub {
    font-size: 29px;
    letter-spacing: 0.2em;
    margin-top: 6px;
  }
</style>
</head>
<body>
<main class="canvas">

  <section class="card card--details" aria-label="Business card, contact side">
    <div class="card-surface"></div>
    <p class="brand-name">Meridian<small>Construction</small></p>
    <svg class="lbp-badge" viewBox="0 0 62 62" role="img" aria-label="Licensed building practitioner badge">
      <circle cx="31" cy="31" r="30" fill="var(--badge-fill)"/>
      <circle cx="31" cy="31" r="24" fill="none" stroke="var(--badge-ring)" stroke-width="1.5"/>
    </svg>
    <div class="holder">
      <p class="holder-name">Tom Halvick</p>
      <p class="holder-role">DIRECTOR</p>
    </div>
    <dl class="contact-list">
      <dt>Address:</dt>
      <dd>48 Wendle place,Ashgrove park 2091<br>Auckland LBP#BP804317</dd>
      <dt>Mobile:</dt>
      <dd>0217364820</dd>
      <dt>Email:</dt>
      <dd>Meridian.Construction@quillpost.example</dd>
    </dl>
  </section>

  <section class="card card--brand" aria-label="Business card, brand side">
    <div class="card-surface"></div>
    <div class="brand-lockup">
      <p class="brand-name">Meridian</p>
      <p class="brand-name sub">Construction</p>
    </div>
  </section>

</main>
</body>
</html>
```